Business Card Design for Online Gift Business

Business card design for a new online Canadian company called "Harlow & Reed Gift Crates" selling modern and luxurious gift boxes for every occasion. Items are sourced locally from talented socially-responsible Canadian artisans. Each gift is elegantly presented in a keepsake wood box to ensure a lasting impression.

Industry/Entity Type

E-Commerce

Contact Information for Business Card

Merin Holloway, Proprietor
Brookvale, AB
587-214-3306
www.harlowandreed.ca
hello@harlowandreed.ca

Requirements
Must have
• Gifts from our hands, to your home
• Please also include the symbols for Facebook and Instagram
Nice to have
• **I have attached a few samples of background colors and font colors that I like. I hope this helps in a few directions to try.

```html
<!DOCTYPE html>
<html lang="en">
<head>
<meta charset="utf-8">
<title>Harlow &amp; Reed Gift Crates — Business Card</title>
<link rel="stylesheet" href="https://fonts.googleapis.com/css2?family=Cormorant+Garamond:ital,wght@1,400&family=Ubuntu:ital,wght@0,300;0,400;0,500;1,400&display=swap">
<style>
  :root {
    --backdrop: #8f8f8f;
    --paper: #e8e8e6;
    --charcoal: #2a2a2a;
    --charcoal-soft: #343434;
    --slate: #454545;
    --gold: #ae9e78;
    --gold-light: #c3b694;
    --gold-shade: #8c7d5c;
    --gold-ink: #b4a27d;
    --cream-text: #f3f0e8;
    --icon-grey: #6a6a6a;
    --muted-text: #555555;
  }
  html, body {
    margin: 0;
    padding: 0;
    width: 980px;
    height: 1200px;
    overflow: hidden;
    background: var(--backdrop);
  }
  .canvas {
    position: relative;
    width: 980px;
    height: 1200px;
  }
  .card { position: absolute; display: block; }
  .card--front { left: 126px; top: 132px; }
  .card--back { left: 120px; top: 711px; }

  .fill-paper { fill: var(--paper); }
  .fill-charcoal { fill: var(--charcoal); }
  .fill-charcoal-soft { fill: var(--charcoal-soft); }
  .fill-slate { fill: var(--slate); }
  .fill-gold { fill: var(--gold); }
  .fill-gold-light { fill: var(--gold-light); }
  .fill-gold-shade { fill: var(--gold-shade); }
  .fill-icon { fill: var(--icon-grey); }

  .wordmark {
    font-family: "Ubuntu", sans-serif;
    font-weight: 300;
    fill: var(--gold-ink);
    letter-spacing: 1px;
  }
  .tagline {
    font-family: "Cormorant Garamond", serif;
    font-style: italic;
    font-size: 22px;
    fill: var(--gold-ink);
  }
  .contact {
    font-family: "Ubuntu", sans-serif;
    fill: var(--cream-text);
  }
  .contact--name { font-weight: 500; font-size: 18px; }
  .contact--role { font-weight: 400; font-size: 15px; }
  .contact--phone { font-weight: 400; font-size: 22px; letter-spacing: 0.5px; }
  .contact--web { font-style: italic; font-size: 15px; }
  .contact--city { font-size: 17px; }
  .social {
    font-family: "Ubuntu", sans-serif;
    font-size: 12px;
    fill: var(--muted-text);
  }
  .icon-line { fill: none; stroke: var(--paper); stroke-width: 1.6; }
  .icon-solid { fill: var(--paper); }
</style>
</head>
<body>
<main class="canvas">

  <!-- Front of card -->
  <svg class="card card--front" width="712" height="411" viewBox="0 0 643 371" aria-label="Business card front">
    <defs>
      <g id="side-ribbon">
        <rect class="fill-gold" x="0" y="0" width="62" height="40"/>
        <polygon class="fill-gold-shade" points="101,42 110,48 101,52"/>
        <polygon class="fill-gold-light" points="62,0 110,8 110,48 62,40"/>
      </g>
    </defs>
    <rect class="fill-paper" x="0" y="0" width="643" height="371"/>
    <rect class="fill-charcoal" x="0" y="0" width="62" height="371"/>
    <rect class="fill-slate" x="62" y="0" width="39" height="371"/>
    <rect class="fill-slate" x="546" y="0" width="38" height="371"/>
    <rect class="fill-charcoal" x="584" y="0" width="59" height="371"/>

    <g class="side-ribbons">
      <use href="#side-ribbon" y="44"/>
      <use href="#side-ribbon" y="127"/>
      <use href="#side-ribbon" y="210"/>
      <use href="#side-ribbon" y="287"/>
    </g>

    <g class="clasp">
      <polygon class="fill-gold-shade" points="530,145 543,132 543,145"/>
      <rect class="fill-gold-light" x="530" y="145" width="99" height="81"/>
      <rect class="fill-paper" x="547" y="162" width="70" height="52"/>
    </g>

    <text class="wordmark" x="323" y="185" font-size="54" text-anchor="middle">Harlow &amp; Reed</text>
    <text class="tagline" x="323" y="272" text-anchor="middle">Gifts from our hands, to your home</text>
  </svg>

  <!-- Back of card -->
  <svg class="card card--back" width="713" height="413" viewBox="0 0 644 373" aria-label="Business card back">
    <defs>
      <g id="back-side-ribbon">
        <rect class="fill-gold" x="0" y="0" width="32" height="40"/>
        <polygon class="fill-gold-shade" points="54,42 60,46 54,50"/>
        <polygon class="fill-gold-light" points="32,0 60,7 60,46 32,40"/>
      </g>
      <g id="contact-ribbon">
        <polygon class="fill-gold-shade" points="312,44 322,44 322,60"/>
        <polygon class="fill-gold-light" points="312,8 373,0 373,42 312,44 304,26"/>
        <rect class="fill-gold" x="373" y="0" width="271" height="42"/>
        <circle class="fill-icon" cx="351" cy="22" r="13"/>
      </g>
    </defs>
    <rect class="fill-paper" x="0" y="0" width="644" height="373"/>
    <rect class="fill-charcoal" x="0" y="0" width="32" height="373"/>
    <rect class="fill-slate" x="32" y="0" width="22" height="373"/>
    <rect class="fill-slate" x="322" y="0" width="51" height="373"/>
    <rect class="fill-charcoal-soft" x="373" y="0" width="271" height="373"/>

    <g class="side-ribbons">
      <use href="#back-side-ribbon" y="43"/>
      <use href="#back-side-ribbon" y="127"/>
      <use href="#back-side-ribbon" y="211"/>
      <use href="#back-side-ribbon" y="289"/>
    </g>

    <g class="contact-ribbons">
      <use href="#contact-ribbon" y="30"/>
      <use href="#contact-ribbon" y="117"/>
      <use href="#contact-ribbon" y="204"/>
      <use href="#contact-ribbon" y="293"/>
    </g>

    <g class="icon icon--person">
      <circle class="icon-solid" cx="351" cy="47" r="3.6"/>
      <path class="icon-solid" d="M344,59 a7,6 0 0 1 14,0 z"/>
    </g>
    <g class="icon icon--phone">
      <path class="icon-solid" d="M345,132 l4,-2 l3,6 l-2.5,1.5 q1.5,4 5,6.5 l2,-2 l5,4 l-2,3 q-9,-1 -14.5,-17 z"/>
    </g>
    <g class="icon icon--globe">
      <circle class="icon-line" cx="351" cy="226" r="8"/>
      <ellipse class="icon-line" cx="351" cy="226" rx="3.5" ry="8"/>
      <line class="icon-line" x1="343" y1="226" x2="359" y2="226"/>
    </g>
    <g class="icon icon--pin">
      <path class="icon-solid" d="M351,304 a6,6 0 0 1 6,6 q0,4 -6,11 q-6,-7 -6,-11 a6,6 0 0 1 6,-6 z"/>
      <circle class="fill-icon" cx="351" cy="310" r="2.2"/>
    </g>

    <text class="contact contact--name" x="504" y="45" text-anchor="middle">Merin Holloway</text>
    <text class="contact contact--role" x="504" y="66" text-anchor="middle">Proprietor</text>
    <text class="contact contact--phone" x="502" y="144" text-anchor="middle">587-214-3306</text>
    <text class="contact contact--web" x="504" y="219" text-anchor="middle">hello@harlowandreed.ca</text>
    <text class="contact contact--web" x="504" y="240" text-anchor="middle">www.harlowandreed.ca</text>
    <text class="contact contact--city" x="418" y="319">Brookvale, AB</text>

    <text class="wordmark" x="182" y="170" font-size="31" text-anchor="middle">Harlow &amp; Reed</text>

    <g class="social-links">
      <circle class="fill-icon" cx="76" cy="317" r="9.5"/>
      <text class="social" x="93" y="321">Pagebook.com</text>
      <circle class="fill-icon" cx="76" cy="342" r="9.5"/>
      <text class="social" x="93" y="346">Snapgram.com</text>
    </g>
  </svg>

</main>
</body>
</html>
```